Lernpfad-Muster für Großhändler (interne Verwendung)
Zielgruppe
Die KORVAN Handelsbedarf Deutschland GmbH ist als Teil der KORVAN Group Großhändler und richtet sich mit seinem Sortiment an Gewerbetreibende. Um 'Profi für Profi' zu sein (und zu bleiben), ist konstante Weiterbildung wichtig. Dafür haben die Mitarbeiter - je nach Position - einen umfangreichen Lernpfad, der aus Trainings und Online-Modulen (eLearnings, Webinare...) besteht und aus dem sie frei ihre Weiterbildungsangebote wählen können.
Diese Lernpfade sollen bekannter werden, v.a. neue Kollegen sollen schon am ersten Tag wissen, was sie tun können, um ihren neuen Arbeitgeber, die Kundengruppen, die Produkte, die Strategie etc. kennenzulernen. Azubis sollen hier eine Art 'Lehrplan' vorfinden. Abnehmer sollen auch alle langjährigen Mitarbeiter und auch deren Führungskräfte sein, um Weiterbildung zu besprechen und gezielt zu planen.
Wir wünschen uns von Ihnen ein Muster, das wir nutzen können, um die Lernpfade entsprechend den Positionen auszugestalten. Beispiel: Wir würden gerne Ihr Muster nehmen und daraus ein Angebot für Kassierer und für Menschen am Wareneingang stricken (unterschiedliche Vorschläge für Trainings und eLearnings).
Die Lernpfade werden übers Intranet zur Verfügung gestellt, den Vertragsunterlagen beigelegt (geplant) und über E-Mailverteiler an Schlüsselpersonen weitergegeben.
Das Thema ist eine Fortsetzung der Training-Kampagne (Poster hängt neben weiteren Dokumenten an).
Aufgabenstellung
Die Flyer werden ausschließlich intern verwendet.
Variante: sechsseitiger Wickelpfalz oder in der Mitte geknickt (also vier Seiten)
Größe: A4
Gesetzte Seiten:
Titelseite:
Bitte den Werkelbert verwenden, das Korvan-Logo, das HR-Logo, einen beispielhaften Lernpfad-Titel (z.B. "Mitarbeiter Verkauf" oder "Abteilungsleiter Warenannahme")
Seite Trainings:
Auf einen Blick soll hier ersichtlich sein, dass es sich um Trainings handelt. Großes Piktogramm, Schraffur - wie auch immer.
Piktogramme oder kleine Bildchen (existieren noch nicht; z.B. für Rhetorik, Veränderung, Konflikt, Führung) mit Trainingstitel (z.B. "Führung konkret") und Dauer (1 Tag z.B.). 30 dieser Bildchen müssen auf eine Seite passen.
Farbliche Kennzeichnung: Führung (violett), Produkte (gelb), Systeme (grün), Soft Skills (blau); zur Einarbeitung empfohlene Trainings werden zusätzlich mit einem Sternchen, verpflichtende Trainings zusätzlich mit einem Ausrufezeichen versehen.
Seite Online-Trainings:
Auf einen Blick soll hier ersichtlich sein, dass es sich um Online-Trainings handelt. Großes Piktogramm, Schraffur - wie auch immer.
Piktogramme oder kleine Bildchen (liegen vor; z.B. für LMIV, Hygiene, Arbeitsrecht, Unsere Kunden) mit Trainingstitel und Dauer (30 Minuten z.B.). 30 dieser Bildchen müssen auf eine Seite passen.
Farbliche Kennzeichnung: wie oben

```html
<!DOCTYPE html>
<html lang="de">
<head>
<meta charset="utf-8">
<title>Lernpfad Abteilungsleiter Warenannahme – KORVAN</title>
<link rel="stylesheet" href="https://fonts.googleapis.com/css2?family=Open+Sans:wght@400;600;700;800&display=swap">
<style>
  :root{
    --bg:#f4f4f2;
    --paper:#ffffff;
    --page:#ececec;
    --ink:#333333;
    --ink-soft:#777777;
    --blue:#1f3fd0;
    --yellow:#f5e21b;
    --teal-dark:#0e4a50;
    --teal-mid:#3f8c8a;
    --teal-light:#8cc7bf;
    --photo-grey:#b9c2c6;
    --shadow:0 4px 14px rgba(0,0,0,.18);
  }
  *{box-sizing:border-box;margin:0;padding:0}
  html,body{width:1200px;height:848px;overflow:hidden}
  body{background:var(--bg);font-family:"Open Sans",Arial,sans-serif;color:var(--ink);position:relative}

  /* Cover */
  .cover{position:absolute;left:60px;top:70px;width:300px;height:424px;background:var(--paper);box-shadow:var(--shadow);overflow:hidden}
  .cover-photo{position:absolute;left:0;top:0;width:300px;height:300px;background:radial-gradient(ellipse at 60% 35%,var(--teal-light) 0%,var(--teal-mid) 45%,var(--teal-dark) 100%)}
  .cover-callouts{position:absolute;left:0;top:0;width:300px;height:300px}
  .callout{position:absolute;font-weight:800;font-size:17px;line-height:1.05;letter-spacing:.5px}
  .callout--before{left:22px;top:88px;color:#fff}
  .callout--after{left:188px;top:168px;color:var(--yellow)}
  .cover-title{position:absolute;left:24px;top:322px;font-weight:800;font-size:16px;line-height:1.2;letter-spacing:1.6px;color:var(--blue)}
  .cover-brand{position:absolute;right:22px;bottom:22px;display:flex;align-items:center;gap:8px}
  .hr-badge{width:22px;height:22px;border-radius:50%;background:var(--blue)}
  .brand-name{font-weight:800;font-size:19px;letter-spacing:1px;color:var(--blue)}

  /* Spread */
  .spread{position:absolute;left:500px;top:55px;width:513px;height:365px;display:flex;box-shadow:var(--shadow)}
  .page{position:relative;width:256px;height:365px;background:var(--page);padding:12px 10px 0 10px}
  .page + .page{border-left:2px solid #c9c9c9}
  .page-head{display:flex;align-items:center;gap:8px;height:24px;margin-bottom:14px}
  .page-title{font-weight:800;font-size:12.5px;letter-spacing:1.4px;color:var(--blue)}
  .course-columns{display:flex;gap:6px}
  .course-list{list-style:none;width:115px}
  .course{display:grid;grid-template-columns:13px 1fr 20px;align-items:center;gap:4px;height:19px}
  .course svg{width:12px;height:12px}
  .course-name{font-size:5px;line-height:1.25;color:var(--ink-soft)}
  .course-time{font-size:5px;color:var(--ink-soft);text-align:right;align-self:start;padding-top:3px}

  /* Back page */
  .back{position:absolute;left:807px;top:443px;width:250px;height:354px;background:var(--page);box-shadow:var(--shadow);padding:16px 14px}
  .info{display:grid;grid-template-columns:1fr 1fr;gap:10px;margin-bottom:30px}
  .info-label{font-size:5.4px;font-weight:700;color:var(--ink);margin-bottom:5px}
  .info-value{font-size:4.6px;line-height:1.35;color:var(--ink-soft);word-break:break-all}
  .contacts{display:grid;grid-template-columns:1fr 1fr;row-gap:6px;column-gap:8px}
  .contact{display:flex;gap:5px;height:36px}
  .contact-photo{flex:0 0 50px;height:36px;background:linear-gradient(135deg,#cfd6da,var(--photo-grey))}
  .contact-name{font-size:5px;font-weight:700;color:var(--ink);margin-bottom:4px}
  .contact-role{font-size:4.6px;line-height:1.35;color:var(--ink-soft)}
</style>
</head>
<body>

<svg width="0" height="0" style="position:absolute" aria-hidden="true">
  <defs>
    <symbol id="ico-rhetoric" viewBox="0 0 12 12"><circle cx="5" cy="4" r="2.2" fill="#333"/><path d="M1 12c0-3.2 1.8-4.6 4-4.6s4 1.4 4 4.6z" fill="#333"/><circle cx="10" cy="2" r="1.6" fill="#f5e21b"/></symbol>
    <symbol id="ico-lead" viewBox="0 0 12 12"><circle cx="6" cy="4" r="2.2" fill="#333"/><path d="M2 12c0-3.2 1.8-4.6 4-4.6s4 1.4 4 4.6z" fill="#333"/></symbol>
    <symbol id="ico-change" viewBox="0 0 12 12"><path d="M1 10l3-3 2 2 5-6" stroke="#f5e21b" stroke-width="1.6" fill="none"/></symbol>
    <symbol id="ico-conflict" viewBox="0 0 12 12"><path d="M7 1L3 7h3l-1 4 4-6H6z" fill="#f5e21b"/></symbol>
  </defs>
</svg>

<section class="cover">
  <div class="cover-photo" role="img" aria-label="Werkelbert, ein Mann im Trägerhemd mit Stirnband und Brille, zeigt einen schmalen und einen muskulösen Oberarm vor türkisem Hintergrund"></div>
  <svg class="cover-callouts" viewBox="0 0 300 300" aria-hidden="true">
    <line x1="68" y1="128" x2="72" y2="160" stroke="#fff" stroke-width="1.5"/>
    <circle cx="72" cy="160" r="2.5" fill="#fff"/>
    <line x1="222" y1="130" x2="220" y2="166" stroke="#f5e21b" stroke-width="1.5"/>
    <circle cx="222" cy="130" r="3" fill="#f5e21b"/>
  </svg>
  <p class="callout callout--before">OHNE<br>TRAINING</p>
  <p class="callout callout--after">MIT<br>TRAINING</p>
  <h1 class="cover-title">ABTEILUNGSLEITER<br>WARENANNAHME</h1>
  <div class="cover-brand"><span class="hr-badge"></span><span class="brand-name">KORVAN</span></div>
</section>

<section class="spread">
  <article class="page page--training">
    <header class="page-head">
      <svg width="26" height="20" viewBox="0 0 26 20" aria-hidden="true"><rect x="1" y="1" width="24" height="18" fill="#333" stroke="#f5e21b" stroke-width="2"/><text x="13" y="13.5" fill="#fff" font-size="8" font-weight="700" text-anchor="middle" font-family="Open Sans, sans-serif">1x1</text></svg>
      <h2 class="page-title">TRAINING</h2>
    </header>
    <div class="course-columns">
      <ul class="course-list">
        <li class="course"><svg><use href="#ico-rhetoric"/></svg><span class="course-name">Rhetorik: Compliance - Geschäftsgrundsätze</span><span class="course-time">1,5h</span></li>
        <li class="course"><svg><use href="#ico-lead"/></svg><span class="course-name">Führung: Gleichberechtigung am Arbeitsplatz</span><span class="course-time">1h</span></li>
        <li class="course"><svg><use href="#ico-change"/></svg><span class="course-name">Veränderung: Arbeitsrecht für Aushilfen</span><span class="course-time">30min</span></li>
        <li class="course"><svg><use href="#ico-conflict"/></svg><span class="course-name">Konflikt: Gerechte Konfliktlösung zwischen Mitarbeitern</span><span class="course-time">30min</span></li>
        <li class="course"><svg><use href="#ico-rhetoric"/></svg><span class="course-name">Rhetorik: Compliance - Geschäftsgrundsätze</span><span class="course-time">1,5h</span></li>
        <li class="course"><svg><use href="#ico-lead"/></svg><span class="course-name">Führung: Gleichberechtigung am Arbeitsplatz</span><span class="course-time">1h</span></li>
        <li class="course"><svg><use href="#ico-change"/></svg><span class="course-name">Veränderung: Arbeitsrecht für Aushilfen</span><span class="course-time">30min</span></li>
        <li class="course"><svg><use href="#ico-conflict"/></svg><span class="course-name">Konflikt: Gerechte Konfliktlösung zwischen Mitarbeitern</span><span class="course-time">30min</span></li>
        <li class="course"><svg><use href="#ico-rhetoric"/></svg><span class="course-name">Rhetorik: Compliance - Geschäftsgrundsätze</span><span class="course-time">1,5h</span></li>
        <li class="course"><svg><use href="#ico-lead"/></svg><span class="course-name">Führung: Gleichberechtigung am Arbeitsplatz</span><span class="course-time">1h</span></li>
        <li class="course"><svg><use href="#ico-change"/></svg><span class="course-name">Veränderung: Arbeitsrecht für Aushilfen</span><span class="course-time">30min</span></li>
        <li class="course"><svg><use href="#ico-conflict"/></svg><span class="course-name">Konflikt: Gerechte Konfliktlösung zwischen Mitarbeitern</span><span class="course-time">30min</span></li>
        <li class="course"><svg><use href="#ico-rhetoric"/></svg><span class="course-name">Rhetorik: Compliance - Geschäftsgrundsätze</span><span class="course-time">1,5h</span></li>
        <li class="course"><svg><use href="#ico-lead"/></svg><span class="course-name">Führung: Gleichberechtigung am Arbeitsplatz</span><span class="course-time">1h</span></li>
        <li class="course"><svg><use href="#ico-change"/></svg><span class="course-name">Veränderung: Arbeitsrecht für Aushilfen</span><span class="course-time">30min</span></li>
      </ul>
      <ul class="course-list">
        <li class="course"><svg><use href="#ico-rhetoric"/></svg><span class="course-name">Rhetorik: Compliance - Geschäftsgrundsätze</span><span class="course-time">1,5h</span></li>
        <li class="course"><svg><use href="#ico-lead"/></svg><span class="course-name">Führung: Gleichberechtigung am Arbeitsplatz</span><span class="course-time">1h</span></li>
        <li class="course"><svg><use href="#ico-change"/></svg><span class="course-name">Veränderung: Arbeitsrecht für Aushilfen</span><span class="course-time">30min</span></li>
        <li class="course"><svg><use href="#ico-conflict"/></svg><span class="course-name">Konflikt: Gerechte Konfliktlösung zwischen Mitarbeitern</span><span class="course-time">30min</span></li>
        <li class="course"><svg><use href="#ico-rhetoric"/></svg><span class="course-name">Rhetorik: Compliance - Geschäftsgrundsätze</span><span class="course-time">1,5h</span></li>
        <li class="course"><svg><use href="#ico-lead"/></svg><span class="course-name">Führung: Gleichberechtigung am Arbeitsplatz</span><span class="course-time">1h</span></li>
        <li class="course"><svg><use href="#ico-change"/></svg><span class="course-name">Veränderung: Arbeitsrecht für Aushilfen</span><span class="course-time">30min</span></li>
        <li class="course"><svg><use href="#ico-conflict"/></svg><span class="course-name">Konflikt: Gerechte Konfliktlösung zwischen Mitarbeitern</span><span class="course-time">30min</span></li>
        <li class="course"><svg><use href="#ico-rhetoric"/></svg><span class="course-name">Rhetorik: Compliance - Geschäftsgrundsätze</span><span class="course-time">1,5h</span></li>
        <li class="course"><svg><use href="#ico-lead"/></svg><span class="course-name">Führung: Gleichberechtigung am Arbeitsplatz</span><span class="course-time">1h</span></li>
        <li class="course"><svg><use href="#ico-change"/></svg><span class="course-name">Veränderung: Arbeitsrecht für Aushilfen</span><span class="course-time">30min</span></li>
        <li class="course"><svg><use href="#ico-conflict"/></svg><span class="course-name">Konflikt: Gerechte Konfliktlösung zwischen Mitarbeitern</span><span class="course-time">30min</span></li>
        <li class="course"><svg><use href="#ico-rhetoric"/></svg><span class="course-name">Rhetorik: Compliance - Geschäftsgrundsätze</span><span class="course-time">1,5h</span></li>
        <li class="course"><svg><use href="#ico-lead"/></svg><span class="course-name">Führung: Gleichberechtigung am Arbeitsplatz</span><span class="course-time">1h</span></li>
        <li class="course"><svg><use href="#ico-change"/></svg><span class="course-name">Veränderung: Arbeitsrecht für Aushilfen</span><span class="course-time">30min</span></li>
      </ul>
    </div>
  </article>

  <article class="page page--online">
    <header class="page-head">
      <svg width="24" height="20" viewBox="0 0 24 20" aria-hidden="true"><rect x="1" y="1" width="22" height="14" fill="#f5e21b" stroke="#333" stroke-width="2"/><rect x="9" y="15" width="6" height="3" fill="#333"/><rect x="6" y="18" width="12" height="2" fill="#333"/></svg>
      <h2 class="page-title">ONLINE - TRAINING</h2>
    </header>
    <div class="course-columns">
      <ul class="course-list">
        <li class="course"><svg><use href="#ico-rhetoric"/></svg><span class="course-name">Rhetorik: Compliance - Geschäftsgrundsätze</span><span class="course-time">1,5h</span></li>
        <li class="course"><svg><use href="#ico-lead"/></svg><span class="course-name">Führung: Gleichberechtigung am Arbeitsplatz</span><span class="course-time">1h</span></li>
        <li class="course"><svg><use href="#ico-change"/></svg><span class="course-name">Veränderung: Arbeitsrecht für Aushilfen</span><span class="course-time">30min</span></li>
        <li class="course"><svg><use href="#ico-conflict"/></svg><span class="course-name">Konflikt: Gerechte Konfliktlösung zwischen Mitarbeitern</span><span class="course-time">30min</span></li>
        <li class="course"><svg><use href="#ico-rhetoric"/></svg><span class="course-name">Rhetorik: Compliance - Geschäftsgrundsätze</span><span class="course-time">1,5h</span></li>
        <li class="course"><svg><use href="#ico-lead"/></svg><span class="course-name">Führung: Gleichberechtigung am Arbeitsplatz</span><span class="course-time">1h</span></li>
        <li class="course"><svg><use href="#ico-change"/></svg><span class="course-name">Veränderung: Arbeitsrecht für Aushilfen</span><span class="course-time">30min</span></li>
        <li class="course"><svg><use href="#ico-conflict"/></svg><span class="course-name">Konflikt: Gerechte Konfliktlösung zwischen Mitarbeitern</span><span class="course-time">30min</span></li>
        <li class="course"><svg><use href="#ico-rhetoric"/></svg><span class="course-name">Rhetorik: Compliance - Geschäftsgrundsätze</span><span class="course-time">1,5h</span></li>
        <li class="course"><svg><use href="#ico-lead"/></svg><span class="course-name">Führung: Gleichberechtigung am Arbeitsplatz</span><span class="course-time">1h</span></li>
        <li class="course"><svg><use href="#ico-change"/></svg><span class="course-name">Veränderung: Arbeitsrecht für Aushilfen</span><span class="course-time">30min</span></li>
        <li class="course"><svg><use href="#ico-conflict"/></svg><span class="course-name">Konflikt: Gerechte Konfliktlösung zwischen Mitarbeitern</span><span class="course-time">30min</span></li>
        <li class="course"><svg><use href="#ico-rhetoric"/></svg><span class="course-name">Rhetorik: Compliance - Geschäftsgrundsätze</span><span class="course-time">1,5h</span></li>
        <li class="course"><svg><use href="#ico-lead"/></svg><span class="course-name">Führung: Gleichberechtigung am Arbeitsplatz</span><span class="course-time">1h</span></li>
        <li class="course"><svg><use href="#ico-change"/></svg><span class="course-name">Veränderung: Arbeitsrecht für Aushilfen</span><span class="course-time">30min</span></li>
      </ul>
      <ul class="course-list">
        <li class="course"><svg><use href="#ico-rhetoric"/></svg><span class="course-name">Rhetorik: Compliance - Geschäftsgrundsätze</span><span class="course-time">1,5h</span></li>
        <li class="course"><svg><use href="#ico-lead"/></svg><span class="course-name">Führung: Gleichberechtigung am Arbeitsplatz</span><span class="course-time">1h</span></li>
        <li class="course"><svg><use href="#ico-change"/></svg><span class="course-name">Veränderung: Arbeitsrecht für Aushilfen</span><span class="course-time">30min</span></li>
        <li class="course"><svg><use href="#ico-conflict"/></svg><span class="course-name">Konflikt: Gerechte Konfliktlösung zwischen Mitarbeitern</span><span class="course-time">30min</span></li>
        <li class="course"><svg><use href="#ico-rhetoric"/></svg><span class="course-name">Rhetorik: Compliance - Geschäftsgrundsätze</span><span class="course-time">1,5h</span></li>
        <li class="course"><svg><use href="#ico-lead"/></svg><span class="course-name">Führung: Gleichberechtigung am Arbeitsplatz</span><span class="course-time">1h</span></li>
        <li class="course"><svg><use href="#ico-change"/></svg><span class="course-name">Veränderung: Arbeitsrecht für Aushilfen</span><span class="course-time">30min</span></li>
        <li class="course"><svg><use href="#ico-conflict"/></svg><span class="course-name">Konflikt: Gerechte Konfliktlösung zwischen Mitarbeitern</span><span class="course-time">30min</span></li>
        <li class="course"><svg><use href="#ico-rhetoric"/></svg><span class="course-name">Rhetorik: Compliance - Geschäftsgrundsätze</span><span class="course-time">1,5h</span></li>
        <li class="course"><svg><use href="#ico-lead"/></svg><span class="course-name">Führung: Gleichberechtigung am Arbeitsplatz</span><span class="course-time">1h</span></li>
        <li class="course"><svg><use href="#ico-change"/></svg><span class="course-name">Veränderung: Arbeitsrecht für Aushilfen</span><span class="course-time">30min</span></li>
        <li class="course"><svg><use href="#ico-conflict"/></svg><span class="course-name">Konflikt: Gerechte Konfliktlösung zwischen Mitarbeitern</span><span class="course-time">30min</span></li>
        <li class="course"><svg><use href="#ico-rhetoric"/></svg><span class="course-name">Rhetorik: Compliance - Geschäftsgrundsätze</span><span class="course-time">1,5h</span></li>
        <li class="course"><svg><use href="#ico-lead"/></svg><span class="course-name">Führung: Gleichberechtigung am Arbeitsplatz</span><span class="course-time">1h</span></li>
        <li class="course"><svg><use href="#ico-change"/></svg><span class="course-name">Veränderung: Arbeitsrecht für Aushilfen</span><span class="course-time">30min</span></li>
      </ul>
    </div>
  </article>
</section>

<section class="back">
  <div class="info">
    <div><p class="info-label">Weg ins Trainingsportal:</p><p class="info-value">http://lernportal.korvan-group.example/t/portal/learn</p></div>
    <div><p class="info-label">E-Mailadresse für Rückfragen:</p><p class="info-value">training@korvan.example</p></div>
  </div>
  <div class="contacts">
    <div class="contact"><div class="contact-photo" role="img" aria-label="Porträtfoto Jana Liebrecht"></div><div><p class="contact-name">Jana Liebrecht</p><p class="contact-role">Konfliktmanagement für Führungspersonal</p></div></div>
    <div class="contact"><div class="contact-photo" role="img" aria-label="Porträtfoto Tobias Kranzler"></div><div><p class="contact-name">Tobias Kranzler</p><p class="contact-role">Gleichberechtigung am Arbeitsplatz</p></div></div>
    <div class="contact"><div class="contact-photo" role="img" aria-label="Porträtfoto Gerd Wallmeyer"></div><div><p class="contact-name">Gerd Wallmeyer</p><p class="contact-role">Kaufmännischer Vertrieb</p></div></div>
    <div class="contact"><div class="contact-photo" role="img" aria-label="Porträtfoto Nadine Oberholz"></div><div><p class="contact-name">Nadine Oberholz</p><p class="contact-role">Lagerservice für Lebensmittel</p></div></div>
    <div class="contact"><div class="contact-photo" role="img" aria-label="Porträtfoto Jana Liebrecht"></div><div><p class="contact-name">Jana Liebrecht</p><p class="contact-role">Konfliktmanagement für Führungspersonal</p></div></div>
    <div class="contact"><div class="contact-photo" role="img" aria-label="Porträtfoto Tobias Kranzler"></div><div><p class="contact-name">Tobias Kranzler</p><p class="contact-role">Gleichberechtigung am Arbeitsplatz</p></div></div>
    <div class="contact"><div class="contact-photo" role="img" aria-label="Porträtfoto Gerd Wallmeyer"></div><div><p class="contact-name">Gerd Wallmeyer</p><p class="contact-role">Kaufmännischer Vertrieb</p></div></div>
    <div class="contact"><div class="contact-photo" role="img" aria-label="Porträtfoto Nadine Oberholz"></div><div><p class="contact-name">Nadine Oberholz</p><p class="contact-role">Lagerservice für Lebensmittel</p></div></div>
  </div>
</section>

</body>
</html>
```